Business Card Design Coralgate Airflow Solutions

The Business will be centred around supply and installation of Ventilation for domestic homes and warehousing/workshops, and will be marketed as a Eco friendly means of reducing your carbon footprint and reducing energy consumption.Our suppliers will provide a range of products that will ventilate roof spaces and later will branch into to air transfer within homes for cooling and heating other rooms of the home etc.I would like to see colours that would be commensurate with the logo provided and yet not dominate the logo.Final design should convey a Diverse , professional but friendly service that will suit client needs

Target Market(s)

Domestic home owners and warehousing/workshop businesses

Industry/Entity Type

Business

Contact Information for Business Card

Company Name: Coralgate Airflow Solutions Pty Ltd, ABN: 42 817 359 264, Address: 27 Marrowfen Tulvanna W.A 6289, Email: dale@coralgateairflowsolutions.com.au, Mobile Number: 0461 852 309

Requirements
Nice to have
• A tract art that commensurate of the logo supplied
Should not have
• Font style that opposes logo design

```html
<!DOCTYPE html>
<html lang="en">
<head>
<meta charset="utf-8">
<title>Coralgate Airflow Solutions – Business Card</title>
<link rel="stylesheet" href="https://fonts.googleapis.com/css2?family=Source+Sans+3:ital,wght@0,400;0,700;1,400&display=swap">
<style>
  :root {
    --backdrop: #0e1712;
    --card-white: #ffffff;
    --leaf-green: #6fbe44;
    --maroon: #3f1416;
  }
  * { margin: 0; padding: 0; box-sizing: border-box; }
  html, body {
    width: 1200px;
    height: 901px;
    overflow: hidden;
    background: var(--backdrop);
    font-family: "Source Sans 3", "Myriad Pro", Arial, sans-serif;
  }
  .stage { position: relative; width: 1200px; height: 901px; }
  .card {
    position: absolute;
    width: 602px;
    height: 345px;
    background: var(--card-white);
    overflow: hidden;
  }
  .card__art { position: absolute; inset: 0; width: 100%; height: 100%; }
  .card--front { left: 226px; top: 120px; }
  .card--back { left: 392px; top: 500px; }

  .brand {
    position: absolute;
    left: 40px;
    top: 96px;
    display: flex;
    align-items: center;
    gap: 10px;
    color: var(--maroon);
    font-size: 30px;
    font-weight: 400;
    line-height: 1.2;
    white-space: nowrap;
  }
  .brand__mark {
    width: 16px; height: 16px;
    background: var(--leaf-green);
    flex: none;
  }

  .holder {
    position: absolute;
    right: 30px;
    top: 256px;
    text-align: right;
    color: var(--maroon);
  }
  .holder__name { font-size: 34px; font-weight: 700; line-height: 1; }
  .holder__role {
    font-size: 19px;
    font-style: italic;
    letter-spacing: 3px;
    margin-top: 4px;
    margin-right: 40px;
  }

  .contact {
    position: absolute;
    right: 28px;
    top: 185px;
    text-align: right;
    color: var(--maroon);
    font-size: 15px;
    font-style: normal;
    line-height: 1.3;
  }
  .contact__company { font-size: 20px; font-weight: 700; margin-bottom: 2px; }
</style>
</head>
<body>
<main class="stage">
  <section class="card card--front" aria-label="Business card front">
    <svg class="card__art" viewBox="0 0 602 345" aria-hidden="true">
      <path d="M0,222 Q250,310 602,42 L602,345 L0,345 Z" fill="var(--leaf-green)"/>
      <path d="M0,222 Q250,310 602,42" fill="none" stroke="var(--maroon)" stroke-width="6"/>
    </svg>
    <div class="brand"><span class="brand__mark"></span>Coralgate Airflow Solutions</div>
    <div class="holder">
      <p class="holder__name">Rena Okafor</p>
      <p class="holder__role">Director</p>
    </div>
  </section>

  <section class="card card--back" aria-label="Business card back">
    <svg class="card__art" viewBox="0 0 602 345" aria-hidden="true">
      <path d="M0,0 L602,0 L602,78 Q240,120 70,345 L0,345 Z" fill="var(--leaf-green)"/>
      <path d="M602,78 Q240,120 70,345" fill="none" stroke="var(--maroon)" stroke-width="6"/>
    </svg>
    <address class="contact">
      <p class="contact__company">Coralgate Airflow Solutions Pty Ltd,</p>
      <p>ABN: 42 817 359 264</p>
      <p>27 Marrowfen Tulvanna W.A 6289</p>
      <p>dale@coralgateairflowsolutions.com.au</p>
      <p>0461 852 309</p>
    </address>
  </section>
</main>
</body>
</html>
```